Spray Foam Company Business Card

We need a business card designed for our spray foam insulation and roof coatings business. We handle residential and commercial projects.
Construction
We would like it to say:
R & K Spray
with these bullet points
-foam insulation
-waterproofing roof system
-water proofing foundation systems
website is rksprayfoaminsulation.example (this was just purchased)
office phone : 630-482-9164
And 3 cards with names on them the names are :
Derek Halvorsen
Curtis Pennington
Rob Stallworth
maybe the bullet points can go on the back?
if you go this website it is another division of our company and you can see the font we use in the R & K. We do not want to use the same half circles that it has just the lettering
www.coatedrightforyears.example

```html
<!DOCTYPE html>
<html lang="en">
<head>
<meta charset="utf-8">
<title>R &amp; K Spray Business Card</title>
<link rel="stylesheet" href="https://fonts.googleapis.com/css2?family=Open+Sans:wght@400;600;700&display=swap">
<style>
  :root {
    --backdrop: #2b2b2b;
    --card: #050505;
    --ink: #ffffff;
    --muted: #e6e6e6;
  }
  * { box-sizing: border-box; margin: 0; padding: 0; }
  html, body { width: 1200px; height: 900px; overflow: hidden; }
  body {
    background: var(--backdrop);
    font-family: "Open Sans", Arial, sans-serif;
    color: var(--ink);
    position: relative;
  }
  .card {
    position: absolute;
    left: 250px;
    width: 700px;
    height: 400px;
    background: var(--card);
    box-shadow: 0 10px 30px rgba(0,0,0,0.55);
    overflow: hidden;
  }
  .card--back { top: 30px; }
  .card--front { top: 470px; }

  .wordmark {
    position: absolute;
    display: flex;
    align-items: center;
    gap: 14px;
    font-weight: 600;
    color: var(--ink);
    letter-spacing: 2px;
  }
  .wordmark__dot {
    width: 18px; height: 18px;
    border-radius: 50%;
    background: var(--ink);
  }
  .card--back .wordmark { left: 48px; top: 58px; font-size: 64px; }
  .card--back .site-link {
    position: absolute; left: 130px; top: 178px;
    font-size: 15px; color: var(--muted);
  }
  .services {
    position: absolute; left: 120px; top: 250px;
  }
  .services__title { font-size: 17px; font-weight: 700; margin-bottom: 4px; }
  .services__list { list-style: none; }
  .services__list li {
    position: relative;
    font-size: 17px; line-height: 24px;
    padding-left: 24px;
    color: var(--muted);
  }
  .services__list li::before {
    content: ""; position: absolute; left: 2px; top: 7px;
    width: 11px; height: 11px; border-radius: 50%; background: var(--ink);
  }

  .card--front .wordmark { left: 230px; top: 80px; font-size: 72px; }
  .holder {
    position: absolute; right: 36px; top: 178px;
    font-size: 19px; font-weight: 700; letter-spacing: 1px;
    text-transform: uppercase;
  }
  .divider {
    position: absolute; left: 445px; top: 215px;
    width: 1px; height: 60px; background: var(--ink);
  }
  .contact { position: absolute; left: 40px; bottom: 38px; }
  .contact__row {
    display: flex; align-items: center; gap: 10px;
    font-size: 16px; line-height: 26px; color: var(--muted);
  }
  .contact__row svg { width: 14px; height: 14px; fill: var(--ink); }
  .base-band {
    position: absolute; left: 0; right: 0; bottom: 0;
    height: 14px; background: var(--ink);
  }
  .edge-band {
    position: absolute; right: 0; top: 150px; bottom: 0;
    width: 12px; background: var(--ink);
  }
</style>
</head>
<body>
  <section class="card card--back">
    <div class="wordmark"><span>R &amp; K</span><span class="wordmark__dot"></span></div>
    <p class="site-link">www.coatedrightforyears.example</p>
    <div class="services">
      <p class="services__title">R &amp; K Spray</p>
      <ul class="services__list">
        <li>Foam insulation</li>
        <li>Waterproofing roof system</li>
        <li>Water proofing foundation systems</li>
      </ul>
    </div>
  </section>

  <section class="card card--front">
    <div class="wordmark"><span>R &amp; K</span><span class="wordmark__dot"></span></div>
    <p class="holder">Derek Halvorsen</p>
    <span class="divider"></span>
    <div class="contact">
      <p class="contact__row">
        <svg viewBox="0 0 24 24" aria-hidden="true"><path d="M6.6 10.8a15.1 15.1 0 0 0 6.6 6.6l2.2-2.2c.3-.3.7-.4 1-.2 1.1.4 2.3.6 3.6.6.6 0 1 .4 1 1V20c0 .6-.4 1-1 1A17 17 0 0 1 3 4c0-.6.4-1 1-1h3.5c.6 0 1 .4 1 1 0 1.3.2 2.5.6 3.6.1.3 0 .7-.2 1z"/></svg>
        <span>630-482-9164</span>
      </p>
      <p class="contact__row">
        <svg viewBox="0 0 24 24" aria-hidden="true"><path d="M12 2a10 10 0 1 0 0 20 10 10 0 0 0 0-20zm6.9 6h-2.9a15.7 15.7 0 0 0-1.4-3.6A8 8 0 0 1 18.9 8zM12 4c.8 1.2 1.5 2.5 1.9 4h-3.8c.4-1.5 1.1-2.8 1.9-4zM4.3 14a8 8 0 0 1 0-4h3.4a16.5 16.5 0 0 0 0 4zm.8 2h2.9c.3 1.3.8 2.5 1.4 3.6A8 8 0 0 1 5.1 16zM8 8H5.1a8 8 0 0 1 4.3-3.6C8.8 5.5 8.3 6.7 8 8zm4 12c-.8-1.2-1.5-2.5-1.9-4h3.8c-.4 1.5-1.1 2.8-1.9 4zm2.3-6H9.7a14.7 14.7 0 0 1 0-4h4.6a14.7 14.7 0 0 1 0 4zm.3 5.6c.6-1.1 1.1-2.3 1.4-3.6h2.9a8 8 0 0 1-4.3 3.6zM16.3 14a16.5 16.5 0 0 0 0-4h3.4a8 8 0 0 1 0 4z"/></svg>
        <span>www.rksprayfoaminsulation.example</span>
      </p>
    </div>
    <span class="edge-band"></span>
    <span class="base-band"></span>
  </section>
</body>
</html>
```